A Speech Therapy Business needs to update their logo

I need an update to the font and color of my logo to look more appealing. I am looking to open a private practice as a Speech Language Pathologist that caters to adults and children. It needs to be sophisticated and friendly at the same time. I want to keep the silhouette in my logo as is, just update the font and color for "Brightpath".
Industry/Entity Type
Business
Contact Information for Business Card
I want the business card to have my logo, my name (Odile Varn, CCC-SLP, TSSLD) and that I am a Bilingual Speech Language Pathologist. Also, include my phone number, (718) 555-0193. Include my website, Brightpathslp.example, and email address, odilevarn@brightpathslp.example
Look and feel

```html
<!DOCTYPE html>
<html lang="en">
<head>
<meta charset="utf-8">
<title>Brightpath – Business Card</title>
<link href="https://fonts.googleapis.com/css2?family=Roboto+Slab:wght@400;700&family=Open+Sans:wght@400;600&display=swap" rel="stylesheet">
<style>
  :root {
    --stage: #e6e6e9;
    --ink: #0c0c0c;
    --paper: #ffffff;
    --rose: #e61c4d;
    --rule: #8a8a8a;
    --text-dark: #1a1a1a;
  }
  * { box-sizing: border-box; margin: 0; padding: 0; }
  html, body {
    width: 1200px; height: 800px; overflow: hidden;
    background: var(--stage);
  }
  .sheet {
    position: relative; width: 1200px; height: 800px;
    display: flex; align-items: center; justify-content: center; gap: 60px;
  }
  .card {
    position: relative; width: 460px; height: 460px;
    border-radius: 30px; overflow: hidden;
    box-shadow: 0 12px 30px rgba(0,0,0,0.18);
  }

  /* Front */
  .card--front { background: var(--ink); }
  .front-logo {
    position: absolute; left: 50%; top: 50%;
    transform: translate(-50%, -56%);
    display: flex; flex-direction: column; align-items: center; gap: 22px;
  }
  .front-logo__figures {
    width: 250px; height: 120px; border-radius: 6px;
    background: linear-gradient(110deg, #f2f2f2 0%, #d8d8d8 100%);
  }
  .front-logo__name {
    font-family: "Roboto Slab", serif; font-weight: 400;
    font-size: 56px; letter-spacing: 2px; text-transform: uppercase;
    color: var(--rose);
  }
  .front-edge {
    position: absolute; left: 0; bottom: 0; width: 100%; height: 12px;
    display: flex;
  }
  .front-edge__red { flex: 0 0 55%; background: var(--rose); }
  .front-edge__white { flex: 1; background: var(--paper); }

  /* Back */
  .card--back { background: var(--paper); }
  .back-figures {
    position: absolute; left: 0; bottom: 66px;
    width: 230px; height: 220px;
    background: linear-gradient(160deg, #2a2a2a 0%, #0c0c0c 100%);
    border-radius: 0 120px 0 0;
  }
  .back-band {
    position: absolute; left: 0; bottom: 0; width: 100%; height: 66px;
    background: var(--rose);
    display: flex; align-items: center; padding-left: 40px;
  }
  .back-band__web {
    font-family: "Open Sans", sans-serif; font-size: 17px;
    color: var(--paper);
  }
  .contact {
    position: absolute; right: 32px; top: 46px; width: 330px;
    text-align: right;
    font-family: "Roboto Slab", serif; color: var(--text-dark);
  }
  .contact__name {
    font-weight: 700; font-size: 21px; color: var(--rose);
    text-transform: uppercase; letter-spacing: 0.3px;
  }
  .contact__title { font-size: 15px; margin-top: 4px; }
  .contact__rule {
    margin: 18px 0 12px auto; width: 240px; height: 1px; background: var(--rule);
  }
  .contact__label { font-size: 11px; color: var(--rose); }
  .contact__value { font-size: 15px; margin-bottom: 8px; }
  .contact__value--email { font-size: 13.5px; }
</style>
</head>
<body>
<main class="sheet">

  <section class="card card--front" aria-label="Card front">
    <div class="front-logo">
      <div class="front-logo__figures" role="img" aria-label="White silhouettes of a family walking hand in hand, adults to small children"></div>
      <div class="front-logo__name">Brightpath</div>
    </div>
    <div class="front-edge">
      <span class="front-edge__red"></span>
      <span class="front-edge__white"></span>
    </div>
  </section>

  <section class="card card--back" aria-label="Card back">
    <div class="contact">
      <p class="contact__name">Odile Varn, CCC-SLP, TSSLD</p>
      <p class="contact__title">Bilingual Speech Language Pathologist</p>
      <div class="contact__rule"></div>
      <p class="contact__label">Phone:</p>
      <p class="contact__value">(718) 555-0193</p>
      <p class="contact__label">Email:</p>
      <p class="contact__value contact__value--email">odilevarn@brightpathslp.example</p>
      <div class="contact__rule"></div>
    </div>
    <div class="back-figures" role="img" aria-label="Black silhouettes of a family walking hand in hand"></div>
    <div class="back-band">
      <span class="back-band__web">www.Brightpathslp.example</span>
    </div>
  </section>

</main>
</body>
</html>
```